Oil and Gas Exploration and Production company needs a business card design

We need a business card design using our logo and colors in the logo. We want a mainstream design.

```html
<!DOCTYPE html>
<html lang="en">
<head>
<meta charset="utf-8">
<title>Varda Oil &amp; Gas – Business Card</title>
<link href="https://fonts.googleapis.com/css2?family=Roboto+Slab:wght@700&family=Montserrat:wght@700&family=Open+Sans:wght@400&display=swap" rel="stylesheet">
<style>
  :root {
    --bg: #2b2b2b;
    --card-dark: #141414;
    --card-light: #ffffff;
    --gold: #c9a03d;
    --ink: #111111;
  }
  * { margin: 0; padding: 0; box-sizing: border-box; }
  html, body { width: 1200px; height: 942px; overflow: hidden; }
  body {
    background: var(--bg);
    position: relative;
    font-family: "Open Sans", Arial, sans-serif;
  }
  .card {
    position: absolute;
    left: 300px;
    width: 600px;
    height: 343px;
    border-radius: 26px;
  }
  .card--back { top: 90px; background: var(--card-dark); }
  .card--front { top: 509px; background: var(--card-light); }

  .brand {
    display: flex;
    align-items: center;
    gap: 12px;
  }
  .brand__dot {
    width: 26px; height: 26px; border-radius: 50%;
    background: var(--gold);
    flex: none;
  }
  .brand__name {
    font-family: "Roboto Slab", Georgia, serif;
    font-weight: 700;
    font-size: 34px;
    line-height: 1;
    white-space: nowrap;
  }

  /* back */
  .card--back .brand {
    position: absolute; left: 0; right: 0; top: 120px;
    justify-content: center;
  }
  .card--back .brand__name { color: var(--gold); }
  .card--back .brand__dot { background: var(--gold); }
  .website-line {
    position: absolute; left: 0; right: 0; top: 210px;
    text-align: center;
    color: var(--gold);
    font-size: 15px;
    letter-spacing: 3px;
  }

  /* front */
  .card--front .brand {
    position: absolute; left: 44px; top: 150px;
  }
  .card--front .brand__name { color: var(--ink); font-size: 28px; }
  .divider {
    position: absolute; left: 330px; top: 70px;
    width: 2px; height: 205px;
    background: var(--gold);
  }
  .contact {
    position: absolute; left: 360px; top: 78px;
  }
  .contact__name {
    font-family: "Montserrat", Arial, sans-serif;
    font-weight: 700;
    font-size: 22px;
    color: var(--ink);
    letter-spacing: 0.5px;
  }
  .contact__title {
    color: var(--gold);
    font-size: 15px;
    margin: 4px 0 22px;
  }
  .contact__row {
    display: flex; align-items: center; gap: 10px;
    font-size: 15px; color: var(--ink);
    margin-bottom: 10px;
  }
  .contact__icon { width: 16px; height: 16px; flex: none; }
</style>
</head>
<body>
  <section class="card card--back" aria-label="Card back">
    <div class="brand">
      <span class="brand__dot"></span>
      <span class="brand__name">Varda Oil &amp; Gas</span>
    </div>
    <p class="website-line">www.yourwebsite.com</p>
  </section>

  <section class="card card--front" aria-label="Card front">
    <div class="brand">
      <span class="brand__dot"></span>
      <span class="brand__name">Varda Oil &amp; Gas</span>
    </div>
    <div class="divider"></div>
    <div class="contact">
      <p class="contact__name">YOUR NAME</p>
      <p class="contact__title">Job Title</p>
      <p class="contact__row">
        <svg class="contact__icon" viewBox="0 0 16 16" aria-hidden="true"><rect x="4" y="1.5" width="8" height="13" rx="1.5" fill="none" stroke="#c9a03d" stroke-width="1.5"/><circle cx="8" cy="12" r="0.9" fill="#c9a03d"/></svg>
        000 000 0000
      </p>
      <p class="contact__row">
        <svg class="contact__icon" viewBox="0 0 16 16" aria-hidden="true"><rect x="1" y="3" width="14" height="10" fill="#c9a03d"/><path d="M1 3 L8 9 L15 3" fill="none" stroke="#fff" stroke-width="1.2"/></svg>
        youremail@xyz.com
      </p>
      <p class="contact__row">
        <svg class="contact__icon" viewBox="0 0 16 16" aria-hidden="true"><g fill="none" stroke="#c9a03d" stroke-width="1.2"><circle cx="8" cy="8" r="6.5"/><ellipse cx="8" cy="8" rx="3" ry="6.5"/><line x1="1.5" y1="8" x2="14.5" y2="8"/></g></svg>
        www.yourwebsite.com
      </p>
    </div>
  </section>
</body>
</html>
```